Journeys With Marcella Business Cards

I need a business card design for my upscale Travel Agency.
Attached you can find my logo.
I would like to include the following:
- Name
- Title
- Phone Number
- Email
- Website
- and then something like: Follow us: JourneysWithMarcella (and then social media icons in color).
The logo should be in the front and then also the back.
I am also attaching a design that I liked (mostly for the layout) but open to any suggestions
Industry/Entity Type
Travel Agent
Contact Information for Business Card
Name: Marcella Dorn
Title: Travel Designer / Owner
Phone: 415-927-3308
Email: marcella@journeyswithmarcella-example.com
Website: www.JourneysWithMarcella-example.com
Social Media Handles for FB,IG, Twitter: JourneysWithMarcella
Colors
Designer to choose colors to be used in the design.
Look and feel

```html
<!DOCTYPE html>
<html lang="en">
<head>
<meta charset="utf-8">
<title>Journeys With Marcella – Business Cards</title>
<link href="https://fonts.googleapis.com/css2?family=Montserrat:wght@400;500;600&display=swap" rel="stylesheet">
<style>
  :root {
    --backdrop: #2b2b2b;
    --card: #ffffff;
    --accent: #f5a85a;
    --ink: #3a3a3a;
  }
  * { box-sizing: border-box; margin: 0; padding: 0; }
  html, body {
    width: 1200px; height: 852px; overflow: hidden;
    background: var(--backdrop);
    font-family: "Montserrat", Arial, sans-serif;
  }
  .stage { position: relative; width: 1200px; height: 852px; }
  .card {
    position: absolute; width: 700px; height: 400px;
    background: var(--card); border-radius: 22px;
    box-shadow: 0 10px 30px rgba(0,0,0,.45);
  }
  .card--front { left: 40px; top: 16px; }
  .card--back { right: 40px; top: 436px; }

  .brand { display: flex; align-items: center; gap: 12px; }
  .brand__square { width: 30px; height: 30px; background: var(--accent); flex: none; }
  .brand__name {
    color: var(--accent); font-weight: 600; letter-spacing: .04em;
    text-transform: uppercase; white-space: nowrap;
  }
  .card--front .brand {
    position: absolute; left: 50%; top: 50%; transform: translate(-50%, -50%);
    gap: 14px;
  }
  .card--front .brand__square { width: 58px; height: 58px; }
  .card--front .brand__name { font-size: 30px; letter-spacing: .06em; }

  .back__left { position: absolute; left: 40px; top: 190px; width: 290px; }
  .card--back .brand__name { font-size: 13px; }
  .follow { margin-top: 34px; font-size: 15px; color: var(--ink); white-space: nowrap; }

  .divider {
    position: absolute; left: 350px; top: 110px; width: 2px; height: 150px;
    background: var(--accent);
  }
  .back__right { position: absolute; left: 372px; top: 104px; right: 16px; }
  .person__name {
    font-size: 22px; font-weight: 600; color: var(--accent);
    text-transform: uppercase; letter-spacing: .02em;
  }
  .person__title { font-size: 14px; color: var(--ink); margin-top: 2px; }
  .contacts { list-style: none; margin-top: 14px; }
  .contacts li {
    display: flex; align-items: center; gap: 8px;
    font-size: 11px; color: var(--ink); line-height: 1.9; white-space: nowrap;
  }
  .contacts svg { width: 11px; height: 11px; flex: none; }
  .highlight { color: var(--accent); }
  .socials { display: flex; gap: 8px; margin-top: 14px; margin-left: 20px; }
  .social { width: 34px; height: 34px; background: var(--accent); border-radius: 6px; }
</style>
</head>
<body>
<main class="stage">
  <section class="card card--front" aria-label="Card front">
    <div class="brand">
      <span class="brand__square"></span>
      <span class="brand__name">Journeys With Marcella</span>
    </div>
  </section>

  <section class="card card--back" aria-label="Card back">
    <div class="back__left">
      <div class="brand">
        <span class="brand__square"></span>
        <span class="brand__name">Journeys With Marcella</span>
      </div>
      <p class="follow">Follow us: JourneysWithMarcella</p>
    </div>

    <div class="divider"></div>

    <div class="back__right">
      <h1 class="person__name">Marcella Dorn</h1>
      <p class="person__title">Travel Designer / Owner</p>
      <ul class="contacts">
        <li>
          <svg viewBox="0 0 24 24"><path fill="#f5a85a" d="M6.6 10.8c1.4 2.8 3.8 5.1 6.6 6.6l2.2-2.2c.3-.3.7-.4 1-.2 1.1.4 2.3.6 3.6.6.6 0 1 .4 1 1V20c0 .6-.4 1-1 1C10.6 21 3 13.4 3 4c0-.6.4-1 1-1h3.5c.6 0 1 .4 1 1 0 1.3.2 2.5.6 3.6.1.3 0 .7-.2 1z"/></svg>
          415-927-3308
        </li>
        <li>
          <svg viewBox="0 0 24 24"><rect x="2" y="5" width="20" height="14" rx="1" fill="none" stroke="#f5a85a" stroke-width="2"/><path d="M2 6l10 7 10-7" fill="none" stroke="#f5a85a" stroke-width="2"/></svg>
          marcella@journeyswithmarcella-example.com
        </li>
        <li>
          <svg viewBox="0 0 24 24"><circle cx="12" cy="12" r="9.5" fill="none" stroke="#f5a85a" stroke-width="2"/><path d="M2.5 12h19M12 2.5c3 3 3 16 0 19M12 2.5c-3 3-3 16 0 19" fill="none" stroke="#f5a85a" stroke-width="1.6"/></svg>
          <span>www.<span class="highlight">JourneysWithMarcella-example</span>.com</span>
        </li>
      </ul>
      <div class="socials">
        <span class="social" role="img" aria-label="Social network icon placeholder"></span>
        <span class="social" role="img" aria-label="Social network icon placeholder"></span>
        <span class="social" role="img" aria-label="Social network icon placeholder"></span>
      </div>
    </div>
  </section>
</main>
</body>
</html>
```